Business cards and logo for a international shipping company called Harborline Freight LLC. We would like to incorporate the colors red and blue. We would like the theme to be nautical.

Industry/Entity Type

Business

```html
<!DOCTYPE html>
<html lang="en">
<head>
<meta charset="utf-8">
<title>Harborline Freight LLC — Business Cards</title>
<link rel="stylesheet" href="https://fonts.googleapis.com/css2?family=Cinzel:wght@500;600&family=Open+Sans:wght@400;600&display=swap">
<style>
  :root {
    --backdrop: #ebebeb;
    --card-white: #fbfbfb;
    --brand-blue: #0866ae;
    --brand-red: #e8202a;
    --ink: #3a3a3a;
    --paper-shadow: rgba(0, 0, 0, 0.18);
  }
  * { box-sizing: border-box; margin: 0; padding: 0; }
  html, body {
    width: 1200px; height: 900px; overflow: hidden;
    background: var(--backdrop);
  }
  .stage {
    width: 1200px; height: 900px;
    display: flex; align-items: center; justify-content: center; gap: 50px;
  }
  .card {
    position: relative;
    width: 525px; height: 300px;
    box-shadow: 0 8px 22px var(--paper-shadow);
  }
  .card--front { background: var(--card-white); }
  .card--back { background: var(--brand-blue); display: flex; align-items: center; justify-content: center; }

  .holder { position: absolute; left: 34px; top: 30px; }
  .holder__name {
    font-family: 'Cinzel', serif; font-weight: 600; font-size: 17px; letter-spacing: 0.5px;
    color: var(--brand-blue);
  }
  .holder__name .surname { color: var(--brand-red); }
  .holder__title {
    font-family: 'Open Sans', sans-serif; font-size: 11px; color: var(--ink); margin-top: 1px;
  }

  .contact { position: absolute; left: 34px; top: 122px; list-style: none; }
  .contact li {
    display: flex; align-items: center; gap: 7px;
    font-family: 'Open Sans', sans-serif; font-size: 11.5px; color: var(--ink); line-height: 18px;
  }
  .contact svg { width: 10px; height: 10px; fill: var(--brand-blue); flex: none; }

  .wordmark {
    display: flex; align-items: center; gap: 10px;
    font-family: 'Cinzel', serif; font-weight: 600; letter-spacing: 1px; white-space: nowrap;
  }
  .wordmark__dot { border-radius: 50%; flex: none; }
  .card--front .wordmark { position: absolute; right: 34px; top: 150px; font-size: 22px; color: var(--brand-blue); }
  .card--front .wordmark__dot { width: 18px; height: 18px; background: var(--brand-red); }
  .card--back .wordmark { font-size: 28px; color: #ffffff; }
  .card--back .wordmark__dot { width: 22px; height: 22px; background: #ffffff; }

  .address {
    position: absolute; right: 34px; bottom: 30px; text-align: right;
    font-family: 'Open Sans', sans-serif; font-size: 12px; color: var(--ink); line-height: 17px;
  }
</style>
</head>
<body>
<main class="stage">
  <section class="card card--front">
    <div class="holder">
      <p class="holder__name">Daniel <span class="surname">Moreau</span></p>
      <p class="holder__title">Managing Director</p>
    </div>

    <ul class="contact">
      <li>
        <svg viewBox="0 0 10 10"><path d="M2 0.5 L3.6 0.5 L4.2 3 L3 3.8 C3.6 5.2 4.8 6.4 6.2 7 L7 5.8 L9.5 6.4 L9.5 8 C9.5 9 8.6 9.6 7.6 9.4 C4.4 8.6 1.4 5.6 0.6 2.4 C0.4 1.4 1 0.5 2 0.5 Z"/></svg>
        (044)987654321
      </li>
      <li>
        <svg viewBox="0 0 10 10"><path d="M0 2 H10 V8.5 H0 Z M0.8 2.6 L5 5.6 L9.2 2.6 L9.2 2.8 L5 6.4 L0.8 2.8 Z" fill-rule="evenodd"/></svg>
        info@harborlinefreight.com
      </li>
      <li>
        <svg viewBox="0 0 10 10"><circle cx="5" cy="5" r="4.6"/><path d="M1 5 H9 M5 0.6 C3 3 3 7 5 9.4 M5 0.6 C7 3 7 7 5 9.4" stroke="#fbfbfb" stroke-width="0.8" fill="none"/></svg>
        www.harborlinefreight.com
      </li>
    </ul>

    <div class="wordmark">
      <span class="wordmark__dot"></span>
      <span>Harborline Freight</span>
    </div>

    <address class="address" style="font-style: normal;">
      58, Quay Street,<br>Portland, 04101
    </address>
  </section>

  <section class="card card--back">
    <div class="wordmark">
      <span class="wordmark__dot"></span>
      <span>Harborline Freight</span>
    </div>
  </section>
</main>
</body>
</html>
```